High Tech Real Estate Startup needs a business card

We are developing an innovative real estate marketing product based around advanced search and virtual reality.

We talk to people, we need business cards.

Target Market(s)

The target market is technology professionals and realtors.

Contact Information for Business Card

The information to be included will include

Name
Title
Phone Number
E-mail Address
www.quelzo.com

It should use simple iconography for each one of those fields.

Font styles to use
Other font styles liked:
• Co, Jubilat, Avenir

Colors

Designer to choose colors to be used in the design.

Requirements
Must have
• Clean aesthetic,
• Good use of negative space.
• It should use our company logo, shown in the attached file. It is able to use the negative of that logo (coloured font and white background) and I have attached other acceptable accent colours in a swatch file.
Should not have
• Should not be too busy
• No extraneous text (slogans, tag lines etc)

```html
<!DOCTYPE html>
<html lang="en">
<head>
<meta charset="utf-8">
<title>Quelzo Business Card</title>
<link rel="stylesheet" href="https://fonts.googleapis.com/css2?family=Nunito+Sans:wght@400;600;700&display=swap">
<style>
  :root {
    --teal: #00a9b1;
    --teal-deep: #0b8289;
    --ink: #4a4a4a;
    --paper: #ffffff;
    --backdrop: #3b3b3b;
  }
  * { margin: 0; padding: 0; box-sizing: border-box; }
  html, body {
    width: 1200px; height: 1200px; overflow: hidden;
    background: var(--backdrop);
    font-family: "Nunito Sans", "Helvetica Neue", Arial, sans-serif;
  }
  .sheet {
    position: relative; width: 1200px; height: 1200px;
    display: flex; align-items: center; justify-content: center; gap: 40px;
  }
  .card { position: relative; width: 540px; height: 324px; overflow: hidden; }

  /* front */
  .card--front { background: var(--paper); }
  .front__brand {
    position: absolute; left: 22px; top: 12px;
    font-size: 60px; font-weight: 600; letter-spacing: 2px;
    color: var(--teal); line-height: 1;
  }
  .front__person { position: absolute; right: 28px; top: 110px; text-align: right; }
  .front__name { font-size: 23px; font-weight: 700; color: var(--ink); line-height: 1.1; }
  .front__title { font-size: 18px; font-weight: 600; color: var(--teal); line-height: 1.2; }
  .contact-list { position: absolute; left: 22px; top: 196px; list-style: none; }
  .contact-list li {
    display: flex; align-items: center; gap: 7px;
    height: 26.5px; font-size: 14px; color: var(--ink);
  }
  .contact-list svg { width: 17px; height: 17px; flex: none; }

  /* back */
  .card--back { background: var(--teal); }
  .back__brand {
    position: absolute; left: 0; right: 0; top: 122px; text-align: center;
    font-size: 80px; font-weight: 600; letter-spacing: 3px;
    color: var(--paper); line-height: 1;
  }
  .back__band {
    position: absolute; left: 18px; right: 18px; top: 281px; height: 14px;
    background: linear-gradient(90deg, rgba(255,255,255,0) 0%, #ffffff 30%, #ffffff 70%, rgba(255,255,255,0) 100%);
  }
  .back__url {
    position: absolute; left: 0; right: 0; top: 279px; text-align: center;
    font-size: 13px; font-weight: 700; color: var(--teal-deep); line-height: 18px;
  }
</style>
</head>
<body>
<main class="sheet">
  <section class="card card--front">
    <div class="front__brand">QUELZO</div>
    <div class="front__person">
      <p class="front__name">Daniel R. Whitford</p>
      <p class="front__title">Director</p>
    </div>
    <ul class="contact-list">
      <li>
        <svg viewBox="0 0 20 20" aria-hidden="true"><circle cx="10" cy="10" r="10" fill="var(--teal)"/><path d="M10 4.5a3.6 3.6 0 0 0-3.6 3.6c0 2.7 3.6 6.9 3.6 6.9s3.6-4.2 3.6-6.9A3.6 3.6 0 0 0 10 4.5zm0 5a1.4 1.4 0 1 1 0-2.8 1.4 1.4 0 0 1 0 2.8z" fill="#fff"/></svg>
        2391 Ashbury Lane Northport, NY 11768
      </li>
      <li>
        <svg viewBox="0 0 20 20" aria-hidden="true"><circle cx="10" cy="10" r="10" fill="var(--teal)"/><path d="M7.2 5c.4 0 .6.2.8.6l.7 1.7c.1.4 0 .7-.3.9l-.7.6c.5 1.1 1.4 2 2.5 2.5l.6-.7c.2-.3.5-.4.9-.3l1.7.7c.4.2.6.4.6.8v1.3c0 .6-.5 1-1.1.9C9.4 13.7 6.3 10.6 6 7.1 5.9 6.5 6.3 6 6.9 6z" fill="#fff"/></svg>
        555-014-7826
      </li>
      <li>
        <svg viewBox="0 0 20 20" aria-hidden="true"><circle cx="10" cy="10" r="10" fill="var(--teal)"/><rect x="5" y="6.5" width="10" height="7" rx="1" fill="#fff"/><path d="M5.4 7l4.6 3.6L14.6 7" fill="none" stroke="var(--teal)" stroke-width="1"/></svg>
        info@quelzo.com
      </li>
      <li>
        <svg viewBox="0 0 20 20" aria-hidden="true"><circle cx="10" cy="10" r="10" fill="var(--teal)"/><g fill="none" stroke="#fff" stroke-width="1.1"><circle cx="10" cy="10" r="5"/><ellipse cx="10" cy="10" rx="2.2" ry="5"/><path d="M5 10h10"/></g></svg>
        www.quelzo.com
      </li>
    </ul>
  </section>

  <section class="card card--back">
    <div class="back__brand">QUELZO</div>
    <div class="back__band"></div>
    <div class="back__url">www.quelzo.com</div>
  </section>
</main>
</body>
</html>
```